Business Landing Page for SEO Company

Need the landing page of the website designed - I will provide the copy, will need to include details of my company and the services offered, about us, testimonials, faq, etc., and all these elements will need to be arranged graphically on the page.

I want something similar to this: https://pebrovault.com/

Not in terms of color or theme or anything, but we offer a similar service and want to display similar information.

Th services we provide are:

Premium Links
Monthly Links Subscription
Link Insertions

Need to advertise them on the front page. Additionally need a place for testimonials, company details, etc.,

We already have logo for the website. Please use the attached file to insert the logo within the overal design.

Target Market(s)

SEO marketers and agencies

Number of Pages Required

1 page

```html
<!DOCTYPE html>
<html lang="en">
<head>
<meta charset="utf-8">
<title>Linkora SEO – Monthly Links Subscription</title>
<link href="https://fonts.googleapis.com/css2?family=Mulish:wght@400;600;700;800;900&family=Lato:wght@400;700&display=swap" rel="stylesheet">
<style>
:root{
  --orange:#f26a1b;
  --blue:#2b74da;
  --navy:#0f1538;
  --ink:#1f1f1f;
  --text:#555a60;
  --muted:#8a8f96;
  --line:#e3e3e3;
  --soft:#f1f1f1;
  --white:#ffffff;
}
*{box-sizing:border-box;margin:0;padding:0}
html,body{width:1200px;height:5177px;overflow:hidden}
body{position:relative;background:var(--white);font-family:'Lato',sans-serif;color:var(--text)}
.abs{position:absolute}
h1,h2,h3,h4{font-family:'Mulish',sans-serif;color:var(--ink)}
.btn{position:absolute;display:flex;align-items:center;justify-content:center;font-family:'Mulish',sans-serif;font-weight:800;color:var(--white);text-transform:uppercase;letter-spacing:.3px}
.btn-orange{background:var(--orange)}
.btn-blue{background:var(--blue)}

/* hero */
.hero{left:0;top:0;width:1200px;height:776px;background:linear-gradient(180deg,#4a4f57 0%,#6d737a 45%,#3b3f45 100%)}
.hero-shade{left:0;top:0;width:1200px;height:776px;background:rgba(20,24,30,.35)}
.brand{font-family:'Mulish',sans-serif;font-weight:800;color:var(--white);font-size:50px;letter-spacing:-.5px;line-height:1}
.nav{left:345px;top:68px;display:flex}
.nav a{font-family:'Mulish',sans-serif;font-weight:700;font-size:15px;color:var(--white);text-decoration:none;margin-right:29px}
.hero-title{left:0;top:318px;width:1200px;text-align:center;color:var(--white);font-size:62px;font-weight:900}
.hero-sub{left:0;top:390px;width:1200px;text-align:center;color:var(--white);font-family:'Mulish',sans-serif;font-size:38px;font-weight:400}

/* services */
.svc{position:absolute;background:var(--white);box-shadow:0 4px 18px rgba(0,0,0,.12);text-align:center;padding:0 28px}
.svc h3{font-size:15px;font-weight:800;letter-spacing:.4px;margin-bottom:18px}
.svc p{font-size:12.5px;line-height:21px}
.svc .ico{margin:40px auto 22px;display:block}

/* featured */
.feat-title{left:0;top:1186px;width:1200px;text-align:center;font-size:20px;font-weight:800}
.feat-row{left:170px;top:1254px;width:880px;display:flex;justify-content:space-between;align-items:center}
.feat-row span{font-family:'Mulish',sans-serif;font-weight:900;font-size:16px;color:#222;line-height:17px;text-align:center}

/* about */
.eyebrow{font-family:'Mulish',sans-serif;color:var(--orange);font-weight:700;font-size:18px}
.rule{position:absolute;height:3px;background:#8a8a8a;width:64px}
.body-copy{font-size:13.5px;line-height:22px}

/* testimonials */
.t-card{position:absolute;background:var(--white);border-radius:8px;text-align:center;padding:0 24px}
.t-card p{font-size:12.5px;line-height:20.5px}
.t-name{position:absolute;text-align:center;font-family:'Mulish',sans-serif;font-size:13px;color:var(--white)}
.stars{color:#ffcc00;font-size:16px;letter-spacing:2px}

/* why */
.why{position:absolute;width:280px}
.why h4{font-size:16px;font-weight:800;margin:26px 0 16px}
.why p{font-size:12.5px;line-height:21px}
.why-ico{width:104px;height:104px;border:3px solid var(--orange);border-radius:50%;display:flex;align-items:center;justify-content:center}

/* faq */
.faq-q{position:absolute;left:142px;width:518px;display:flex;justify-content:space-between;align-items:center;font-size:14.5px;color:var(--text)}
.faq-dot{width:17px;height:17px;border-radius:50%;background:var(--orange);display:flex;align-items:center;justify-content:center}

/* quote form */
.field{position:absolute;border:1px solid #c9c9c9;border-radius:26px;font-size:13px;color:#666;padding:0 20px;display:flex;align-items:center}

/* footer */
.foot{left:0;top:4692px;width:1200px;height:485px;background:var(--navy)}
.foot h4{color:var(--white);font-size:17px;font-weight:800;letter-spacing:.3px}
.foot p,.foot li{color:#cfd3e6;font-size:13px;line-height:20px;list-style:none}
</style>
</head>
<body>

<!-- HERO -->
<div class="abs hero" role="img" aria-label="Photo of a presenter pointing at an SEO mind map on a whiteboard in front of a team at laptops"></div>
<div class="abs hero-shade"></div>
<div class="abs brand" style="left:62px;top:52px">Linkora</div>
<nav class="abs nav">
  <a href="#">HOME</a><a href="#">ABOUT</a><a href="#">SERVICES</a><a href="#">FAQ</a><a href="#">TESTIMONIALS</a><a href="#" style="margin-left:45px">CONTACT</a>
</nav>
<div class="btn btn-orange" style="left:945px;top:62px;width:192px;height:40px;font-size:13px">Getting Started</div>
<h1 class="abs hero-title">Linkora SEO</h1>
<div class="abs hero-sub">Monthly Links Subscription</div>
<div class="btn btn-orange" style="left:507px;top:453px;width:186px;height:40px;font-size:15px">Learn More</div>

<!-- SERVICES -->
<div class="svc" style="left:142px;top:728px;width:276px;height:370px">
  <svg class="ico" width="80" height="80" viewBox="0 0 80 80" fill="none" stroke="#2b74da" stroke-width="2.5"><circle cx="22" cy="30" r="7"/><circle cx="58" cy="30" r="7"/><path d="M10 60v-12q0-8 12-8t12 8v12M46 60v-12q0-8 12-8t12 8v12"/><rect x="30" y="8" width="20" height="14"/><path d="M18 66h44"/></svg>
  <h3>PREMIUM LINKS</h3>
  <p>Sed ut perspiciatis unde omnis iste natus error sit voluptatem accntium doloremque laudantium, totam rem aperiam, eaque ipsa quae ab illo inventore veritatis</p>
  <div class="btn btn-blue" style="left:88px;top:298px;width:106px;height:32px;font-size:11px">Learn More</div>
</div>
<div class="svc" style="left:418px;top:705px;width:362px;height:396px;border-bottom:4px solid var(--orange);border-radius:8px 8px 0 0;z-index:2">
  <svg class="ico" width="84" height="84" viewBox="0 0 84 84" fill="none" stroke="#f26a1b" stroke-width="2.5"><rect x="6" y="14" width="64" height="58" rx="4"/><path d="M6 28h64M20 6v14M56 6v14"/><g stroke-width="2"><rect x="14" y="36" width="8" height="7"/><rect x="28" y="36" width="8" height="7"/><rect x="42" y="36" width="8" height="7"/><rect x="14" y="50" width="8" height="7"/><rect x="28" y="50" width="8" height="7"/></g><circle cx="64" cy="62" r="13" fill="#fff"/><path d="M58 62l5 5 8-9"/></svg>
  <h3>MONTHLY LINKS SUBSCRIPTION</h3>
  <p>Sed ut perspiciatis unde omnis iste natus error sit voluptatem accntium doloremque lauantium, totam rem aperiam, eaque ipsa quae ab illo inventore veritatis Sed ut perspiciatis unde omnis iste natus voluptatem accntium</p>
  <div class="btn btn-orange" style="left:124px;top:322px;width:116px;height:32px;font-size:11px">Learn More</div>
</div>
<div class="svc" style="left:780px;top:728px;width:275px;height:370px">
  <svg class="ico" width="80" height="80" viewBox="0 0 80 80" fill="none" stroke="#2b74da" stroke-width="2.5"><rect x="10" y="8" width="60" height="34" rx="2"/><path d="M22 20h18M22 30h30"/><circle cx="20" cy="54" r="6"/><circle cx="40" cy="54" r="6"/><circle cx="60" cy="54" r="6"/><path d="M10 74q0-10 10-10t10 10M30 74q0-10 10-10t10 10M50 74q0-10 10-10t10 10"/></svg>
  <h3>LINK INSERTIONS</h3>
  <p>Sed ut perspiciatis unde omnis iste natus error sit voluptatem accntium doloremque laudantium, totam rem aperiam, eaque ipsa quae ab illo inventore veritatis</p>
  <div class="btn btn-blue" style="left:79px;top:298px;width:116px;height:32px;font-size:11px">Learn More</div>
</div>

<!-- FEATURED -->
<h2 class="abs feat-title">FEATURED IN</h2>
<div class="abs feat-row">
  <span>MARKET<br>LEDGER</span><span>RANK<br>FORGE</span><span>Crawlwise</span><span>KESTREL</span><span>Search Council</span><span>Index<br>Observer</span>
</div>

<!-- ABOUT -->
<div class="abs eyebrow" style="left:142px;top:1413px">About Linkora</div>
<h2 class="abs" style="left:142px;top:1446px;width:380px;font-size:28px;font-weight:800;line-height:38px">Nemo enim ipsam voluptatem quia voluptas</h2>
<div class="rule" style="left:142px;top:1537px"></div>
<p class="abs body-copy" style="left:142px;top:1564px;width:400px">Sed ut perspiciatis unde omnis iste natus error sit voluptatem accusantium doloremque laudantium, totam rem aperiam, eaque ipsa quae ab illo inventore veritatis et quasi architecto beatae vitae dicta sunt explicabo. Nemo enim ipsam voluptatem quia voluptas sit aspernatur aut odit aut fugit, sed quia consequuntur magni dolores eos</p>
<div class="btn btn-orange" style="left:142px;top:1725px;width:164px;height:42px;font-size:14px">Learn More</div>
<div class="abs" style="left:598px;top:1402px;width:466px;height:402px;background:var(--orange)"></div>
<div class="abs" role="img" aria-label="Photo of a smiling team gathered around a desk in a bright office" style="left:590px;top:1394px;width:466px;height:402px;background:linear-gradient(160deg,#c9ccd0 0%,#8f959c 50%,#4d5a6e 100%)"></div>

<!-- TESTIMONIALS -->
<svg class="abs" style="left:0;top:1910px" width="1200" height="790" viewBox="0 0 1200 790">
  <polygon points="0,100 310,5 1200,90 1200,698 880,780 0,695" fill="#2b74da"/>
  <polyline points="0,100 310,5 1200,90" fill="none" stroke="#f26a1b" stroke-width="6"/>
  <polyline points="0,695 880,780 1200,698" fill="none" stroke="#f26a1b" stroke-width="6"/>
</svg>
<h2 class="abs" style="left:0;top:2024px;width:1200px;text-align:center;color:#fff;font-size:36px;font-weight:600">Client Testimonial</h2>
<div class="rule" style="left:558px;top:2088px;width:84px;background:#fff;height:2px"></div>

<div class="t-card" style="left:142px;top:2150px;width:282px;height:254px">
  <svg style="margin:26px auto 14px;display:block" width="40" height="40" viewBox="0 0 40 40"><circle cx="20" cy="20" r="20" fill="#2b74da"/><path d="M11 22q0-8 7-10v3q-3 1-3 5h3v7h-7zM22 22q0-8 7-10v3q-3 1-3 5h3v7h-7z" fill="#fff"/></svg>
  <p>Lorem ipsum dolor sit amet, contetur adipiscing elit, sed do eiusmod tempor incididunt ut labore et dolore magna aliqua. Ut enim ad minim veniam, quis nostrud exercitation ullamco laboris nisi ut aliquip ex ea commodo consequat.</p>
</div>
<div class="t-name" style="left:142px;top:2430px;width:282px"><b>Maren Colby</b><br>Linkora<br><span class="stars">★★★★★</span></div>

<div class="t-card" style="left:420px;top:2140px;width:356px;height:312px;box-shadow:0 6px 18px rgba(0,0,0,.18);z-index:2">
  <svg style="margin:28px auto 14px;display:block" width="42" height="42" viewBox="0 0 40 40"><circle cx="20" cy="20" r="20" fill="#f26a1b"/><path d="M11 22q0-8 7-10v3q-3 1-3 5h3v7h-7zM22 22q0-8 7-10v3q-3 1-3 5h3v7h-7z" fill="#fff"/></svg>
  <p>Sed ut perspiciatis unde omnis iste natus error sit voluptatem accusantium doloremque laudantium, totam rem aperiam, eaque ipsa quae ab illo inventore veritatis et quasi arecto beatae vitae dicta sunt explicabo. Nemo enim ipsam voluptatem quia voluptas sit aspertur aut odit aut fugit, sed quia consequuntur</p>
  <div style="font-family:'Mulish',sans-serif;font-size:13px;color:var(--orange);margin-top:12px;line-height:20px"><b>Maren Colby</b><br>Linkora</div>
</div>
<div class="t-name" style="left:420px;top:2476px;width:356px"><span class="stars">★★★★★</span></div>

<div class="t-card" style="left:772px;top:2150px;width:282px;height:254px">
  <svg style="margin:26px auto 14px;display:block" width="40" height="40" viewBox="0 0 40 40"><circle cx="20" cy="20" r="20" fill="#2b74da"/><path d="M11 22q0-8 7-10v3q-3 1-3 5h3v7h-7zM22 22q0-8 7-10v3q-3 1-3 5h3v7h-7z" fill="#fff"/></svg>
  <p>Lorem ipsum dolor sit amet, contetur adipiscing elit, sed do eiusmod tempor incididunt ut labore et dolore magna aliqua. Ut enim ad minim veniam, quis nostrud exercitation ullamco laboris nisi ut aliquip ex ea commodo consequat.</p>
</div>
<div class="t-name" style="left:772px;top:2430px;width:282px"><b>Maren Colby</b><br>Linkora<br><span class="stars">★★★★★</span></div>

<svg class="abs" style="left:556px;top:2560px" width="90" height="16" viewBox="0 0 90 16"><g fill="#fff"><circle cx="8" cy="8" r="3"/><circle cx="24" cy="8" r="3"/><circle cx="62" cy="8" r="3"/><circle cx="80" cy="8" r="3"/></g><circle cx="43" cy="8" r="6" fill="#f6c343"/></svg>

<!-- WHY CHOOSE -->
<h2 class="abs" style="left:0;top:2770px;width:1200px;text-align:center;font-size:36px;font-weight:800">Why Choose Linkora?</h2>
<div class="rule" style="left:560px;top:2830px;width:80px"></div>
<div class="abs" style="left:438px;top:2895px;width:1px;height:625px;background:var(--line)"></div>
<div class="abs" style="left:767px;top:2895px;width:1px;height:625px;background:var(--line)"></div>
<div class="abs" style="left:142px;top:3195px;width:915px;height:1px;background:var(--line)"></div>

<div class="why" style="left:142px;top:2912px"><div class="why-ico"><svg width="58" height="58" viewBox="0 0 58 58" fill="none" stroke="#333" stroke-width="2"><rect x="8" y="10" width="34" height="38" rx="3"/><path d="M14 18h14M14 24h20"/><circle cx="38" cy="36" r="12" fill="#fff"/><path d="M38 30v12M35 33h5a2 2 0 010 4h-4a2 2 0 000 4h5"/></svg></div><h4>Nemo enim voluptatem</h4><p>Sed ut perspiciatis unde omnis iste natus error sit voluptatem accntium doloremque laudantium, totam rem aperiam, eaque ipsa quae ab illo inventore veritatis</p></div>
<div class="why" style="left:470px;top:2912px"><div class="why-ico"><svg width="58" height="58" viewBox="0 0 58 58" fill="none" stroke="#333" stroke-width="2"><rect x="18" y="6" width="22" height="14"/><circle cx="29" cy="28" r="6"/><path d="M17 46q0-10 12-10t12 10M8 46h42M12 46v8M46 46v8"/></svg></div><h4>Nemo enim voluptatem</h4><p>Sed ut perspiciatis unde omnis iste natus error sit voluptatem accntium doloremque laudantium, totam rem aperiam, eaque ipsa quae ab illo inventore veritatis</p></div>
<div class="why" style="left:786px;top:2912px"><div class="why-ico"><svg width="58" height="58" viewBox="0 0 58 58" fill="none" stroke="#333" stroke-width="2"><rect x="8" y="8" width="34" height="42"/><path d="M16 40V30M23 40V22M30 40V26"/><circle cx="40" cy="38" r="9" fill="#fff"/><path d="M46 44l7 7"/></svg></div><h4>Nemo enim voluptatem</h4><p>Sed ut perspiciatis unde omnis iste natus error sit voluptatem accntium doloremque laudantium, totam rem aperiam, eaque ipsa quae ab illo inventore veritatis</p></div>

<div class="why" style="left:142px;top:3232px"><div class="why-ico"><svg width="58" height="58" viewBox="0 0 58 58" fill="none" stroke="#333" stroke-width="2"><circle cx="26" cy="32" r="16"/><path d="M18 32a8 8 0 0116 0v6h-4M18 32v6h4"/><rect x="34" y="6" width="18" height="12" rx="2"/></svg></div><h4>Nemo enim voluptatem</h4><p>Sed ut perspiciatis unde omnis iste natus error sit voluptatem accntium doloremque laudantium, totam rem aperiam, eaque ipsa quae ab illo inventore veritatis</p></div>
<div class="why" style="left:470px;top:3232px"><div class="why-ico"><svg width="58" height="58" viewBox="0 0 58 58" fill="none" stroke="#333" stroke-width="2"><rect x="6" y="10" width="46" height="30" rx="2"/><path d="M22 48h14M29 40v8"/><rect x="12" y="16" width="14" height="10"/><path d="M32 18h14M32 24h10M12 32h34"/></svg></div><h4>Nemo enim voluptatem</h4><p>Sed ut perspiciatis unde omnis iste natus error sit voluptatem accntium doloremque laudantium, totam rem aperiam, eaque ipsa quae ab illo inventore veritatis</p></div>
<div class="why" style="left:786px;top:3232px"><div class="why-ico"><svg width="58" height="58" viewBox="0 0 58 58" fill="none" stroke="#333" stroke-width="2"><rect x="20" y="6" width="30" height="20" rx="2"/><circle cx="16" cy="30" r="6"/><path d="M6 52V42q0-6 10-6t10 6v10M32 36h14v16"/></svg></div><h4>Nemo enim voluptatem</h4><p>Sed ut perspiciatis unde omnis iste natus error sit voluptatem accntium doloremque laudantium, totam rem aperiam, eaque ipsa quae ab illo inventore veritatis</p></div>

<!-- FAQ -->
<div class="abs" style="left:0;top:3565px;width:718px;height:646px;background:var(--soft)"></div>
<div class="abs" role="img" aria-label="Photo of two smiling colleagues looking at a phone together" style="left:718px;top:3565px;width:482px;height:646px;background:linear-gradient(150deg,#9aa1a8 0%,#c8b8a6 50%,#5a5f66 100%)"></div>
<h2 class="abs" style="left:142px;top:3625px;font-size:38px;font-weight:700">Linkora FAQ</h2>
<div class="faq-q" style="top:3700px;height:24px">Sed ut perspiciatis unde omnis iste natus accusantiu?<span class="faq-dot"><svg width="9" height="9" viewBox="0 0 9 9"><path d="M3 1.5l3 3-3 3" stroke="#fff" stroke-width="1.6" fill="none"/></svg></span></div>
<div class="abs" style="left:142px;top:3750px;width:518px;height:175px;background:#fff"></div>
<div class="faq-q" style="top:3778px;left:166px;width:478px;height:24px">Sed ut perspiciatis unde omnis iste natus accusantiu?<span class="faq-dot"><svg width="9" height="9" viewBox="0 0 9 9"><path d="M1.5 3l3 3 3-3" stroke="#fff" stroke-width="1.6" fill="none"/></svg></span></div>
<p class="abs" style="left:166px;top:3818px;width:470px;font-size:12.5px;line-height:20px">Sed ut perspiciatis unde omnis iste natus error sit voluptatem accusium doloremque laudantium, totam rem aperiam, eaque ipsa quae ab illo inventore veritatis et quasi architecto beatae vitae dicta sunt explicabo. Nemo enim ipsam voluptatem quia voluptas</p>
<div class="faq-q" style="top:3956px;height:24px">Sed ut perspiciatis unde omnis iste natus accusantiu?<span class="faq-dot"><svg width="9" height="9" viewBox="0 0 9 9"><path d="M3 1.5l3 3-3 3" stroke="#fff" stroke-width="1.6" fill="none"/></svg></span></div>
<div class="abs" style="left:142px;top:3998px;width:518px;height:1px;background:#d6d6d6"></div>
<div class="faq-q" style="top:4027px;height:24px">Sed ut perspiciatis unde omnis iste natus accusantiu?<span class="faq-dot"><svg width="9" height="9" viewBox="0 0 9 9"><path d="M3 1.5l3 3-3 3" stroke="#fff" stroke-width="1.6" fill="none"/></svg></span></div>
<div class="abs" style="left:142px;top:4070px;width:518px;height:1px;background:#d6d6d6"></div>
<div class="faq-q" style="top:4100px;height:24px">Sed ut perspiciatis unde omnis iste natus accusantiu?<span class="faq-dot"><svg width="9" height="9" viewBox="0 0 9 9"><path d="M3 1.5l3 3-3 3" stroke="#fff" stroke-width="1.6" fill="none"/></svg></span></div>

<!-- QUOTE -->
<h2 class="abs" style="left:142px;top:4330px;width:320px;font-size:36px;font-weight:900;line-height:44px">Get Your Free Quote</h2>
<p class="abs body-copy" style="left:142px;top:4466px;width:320px;font-size:14.5px;line-height:24px">Sed ut perspiciatis unde omnis iste natus sit voluptatem accusantium doloremque laudantium, totam rem aperiam, eaque ipsa quae ab illo inventore veritatis et quasi architecto beatae vitae dicta</p>
<div class="abs" style="left:525px;top:4292px;width:1px;height:300px;background:var(--line)"></div>
<div class="field" style="left:587px;top:4302px;width:252px;height:48px">First name</div>
<div class="field" style="left:853px;top:4302px;width:250px;height:48px">Last Name</div>
<div class="field" style="left:587px;top:4367px;width:252px;height:48px">Email</div>
<div class="field" style="left:853px;top:4367px;width:250px;height:48px">Phone Number</div>
<div class="field" style="left:587px;top:4432px;width:516px;height:98px;align-items:flex-start;padding-top:18px">Message</div>
<div class="btn btn-orange" style="left:587px;top:4555px;width:152px;height:42px;font-size:14px;border-radius:21px">Submit</div>

<!-- FOOTER -->
<footer class="abs foot">
  <div class="abs" style="left:103px;top:70px;font-family:'Mulish',sans-serif;font-weight:800;font-size:56px;line-height:1;color:var(--blue)">Linkora</div>
  <p class="abs" style="left:103px;top:155px;width:232px;font-size:12.5px">Sed ut perspiciatis unde omnis iste natus error sit vtem accusantium dolorque lam, totam rem aperiam, eaque ipsa quae ab illo</p>
  <div class="abs" style="left:103px;top:266px;display:flex;gap:9px">
    <span style="width:30px;height:30px;border:2px solid #fff;border-radius:50%"></span><span style="width:30px;height:30px;border:2px solid #fff;border-radius:50%"></span><span style="width:30px;height:30px;border:2px solid #fff;border-radius:50%"></span><span style="width:30px;height:30px;border:2px solid #fff;border-radius:50%"></span>
  </div>

  <h4 class="abs" style="left:393px;top:86px">SIGN UP FOR NEWSLETTER</h4>
  <p class="abs" style="left:393px;top:128px;width:280px;font-size:12.5px">excepteur sint occaecat cupidatat non proident, sunt in culpa qui officia deserunt</p>
  <div class="abs" style="left:393px;top:192px;width:273px;height:36px;background:#fff;border-radius:18px;font-size:12px;color:#777;padding:10px 16px">Enter email</div>
  <div class="btn btn-orange" style="left:393px;top:246px;width:138px;height:36px;font-size:13px;border-radius:18px">Subscribe</div>

  <h4 class="abs" style="left:717px;top:88px">CONTACT US</h4>
  <svg class="abs" style="left:718px;top:130px" width="16" height="22" viewBox="0 0 16 22"><path d="M8 0a8 8 0 00-8 8c0 6 8 14 8 14s8-8 8-14a8 8 0 00-8-8z" fill="#fff"/><circle cx="8" cy="8" r="3" fill="#0f1538"/></svg>
  <p class="abs" style="left:753px;top:128px;width:180px">Address.<br>Unit 42, enim ipsam voluptatem quia</p>
  <svg class="abs" style="left:718px;top:205px" width="18" height="18" viewBox="0 0 18 18"><path d="M4 1l3 4-2 2q2 4 6 6l2-2 4 3-2 3Q6 16 1 3z" fill="#fff"/></svg>
  <p class="abs" style="left:753px;top:203px">Phone:<br>555 0142 7781</p>
  <svg class="abs" style="left:718px;top:254px" width="18" height="14" viewBox="0 0 18 14"><rect width="18" height="14" rx="1" fill="#fff"/><path d="M1 1l8 6 8-6" stroke="#0f1538" stroke-width="1.5" fill="none"/></svg>
  <p class="abs" style="left:753px;top:248px">Email:<br>hello@linkora.example</p>

  <h4 class="abs" style="left:968px;top:86px">QUICK LINKS</h4>
  <ul class="abs" style="left:973px;top:123px">
    <li style="line-height:27px">Home</li><li style="line-height:27px">About us</li><li style="line-height:27px">Services</li><li style="line-height:27px">Testimonials</li><li style="line-height:27px">Faq</li><li style="line-height:27px">Contact</li>
  </ul>

  <div class="abs" style="left:0;top:405px;width:1200px;height:1px;background:#262d55"></div>
  <p class="abs" style="left:0;top:437px;width:1200px;text-align:center;font-size:12.5px;color:#fff">Linkora © 2021 All Rights Reserved | Privacy Policy | Terms and Conditions</p>
</footer>

</body>
</html>
```